Computer Service Provider in Need of New Letterhead Design

We are Larkvale Computer Services, a computer/IT services company that provides IT Support, software, hardware, virus monitoring, etc. in Vermont. We are looking for new letterhead, that is both professional and matches the current theme of our business cards & website.
Please note that we want to include the following information:
www.Larkvale.example
802-555-0147
47 Fernwick Hollow Road, Ashbury Falls, VT 05999
Reliable Systems • Friendly Experts • Dependable Results
I will be attaching our logo along with the business card images.
We would love to have the

```html
<!DOCTYPE html>
<html lang="en">
<head>
<meta charset="utf-8">
<title>Larkvale Computer Services – Letterhead</title>
<link href="https://fonts.googleapis.com/css2?family=Oswald:wght@300&family=Nunito+Sans:wght@400;700;800&display=swap" rel="stylesheet">
<style>
  :root {
    --brand-blue: #0553a1;
    --logo-navy: #1d4a78;
    --ink: #333b44;
    --paper: #ffffff;
  }
  * { margin: 0; padding: 0; box-sizing: border-box; }
  html, body { width: 848px; height: 1200px; overflow: hidden; background: var(--paper); }
  .letterhead {
    position: relative;
    width: 848px;
    height: 1200px;
    overflow: hidden;
    font-family: "Nunito Sans", sans-serif;
    color: var(--ink);
  }
  .artwork { position: absolute; inset: 0; width: 848px; height: 1200px; }
  .wordmark {
    position: absolute;
    right: 24px;
    top: 188px;
    text-align: right;
    color: var(--logo-navy);
    font-weight: 800;
  }
  .wordmark-name { display: block; font-size: 48px; line-height: 48px; letter-spacing: -0.5px; }
  .wordmark-sub { display: block; font-size: 20px; line-height: 24px; letter-spacing: 4.6px; margin-right: -4.6px; }
  .tagline {
    position: absolute;
    left: 50px;
    top: 287px;
    font-size: 24.5px;
    color: var(--brand-blue);
    white-space: nowrap;
  }
  .salutation {
    position: absolute;
    left: 58px;
    top: 380px;
    font-family: "Oswald", sans-serif;
    font-weight: 300;
    text-transform: uppercase;
    font-size: 24px;
    line-height: 30px;
    letter-spacing: 1.4px;
    color: var(--ink);
  }
  .letter-body {
    position: absolute;
    left: 75px;
    top: 440px;
    width: 720px;
    font-size: 15.4px;
    line-height: 28.8px;
  }
  .letter-body p + p { margin-top: 28.8px; }
  .sign-off {
    position: absolute;
    left: 58px;
    font-size: 15.4px;
    font-weight: 700;
  }
  .sign-off.closing { top: 886px; }
  .sign-off.name { top: 944px; }
  .sign-off.title { top: 973px; }
  .contact {
    position: absolute;
    left: 92px;
    color: var(--paper);
    font-size: 15.6px;
    display: flex;
    align-items: center;
    gap: 6px;
  }
  .contact svg { width: 20px; height: 20px; fill: var(--paper); }
  .contact.phone { top: 1099px; }
  .contact.address { top: 1128px; }
  .website {
    position: absolute;
    left: 0;
    width: 784px;
    top: 1172px;
    text-align: center;
    color: var(--paper);
    font-size: 15.6px;
  }
</style>
</head>
<body>
<div class="letterhead">
  <svg class="artwork" viewBox="0 0 794 1123" aria-hidden="true">
    <g fill="var(--brand-blue)">
      <polygon points="-60,0 -38,0 -158,245 -180,245"/>
      <polygon points="-25,0 -3,0 -123,245 -145,245"/>
      <polygon points="10,0 32,0 -88,245 -110,245"/>
      <polygon points="45,0 67,0 -53,245 -75,245"/>
      <polygon points="80,0 102,0 -18,245 -40,245"/>
      <polygon points="115,0 137,0 17,245 -5,245"/>
      <polygon points="150,0 172,0 52,245 30,245"/>
      <polygon points="185,0 207,0 87,245 65,245"/>
      <polygon points="220,0 242,0 122,245 100,245"/>
      <polygon points="255,0 277,0 157,245 135,245"/>
      <polygon points="290,0 515,0 560,58 440,245 170,245"/>
      <polygon points="65,1002 794,1002 794,1123 65,1123 27,1068"/>
    </g>
    <g fill="var(--paper)">
      <polygon points="680,1002 694,1002 634,1123 620,1123"/>
      <polygon points="712,1002 726,1002 666,1123 652,1123"/>
      <polygon points="744,1002 758,1002 698,1123 684,1123"/>
      <polygon points="776,1002 790,1002 730,1123 716,1123"/>
      <polygon points="808,1002 822,1002 762,1123 748,1123"/>
      <polygon points="840,1002 854,1002 794,1123 780,1123"/>
    </g>
  </svg>

  <div class="wordmark">
    <span class="wordmark-name">Larkvale</span>
    <span class="wordmark-sub">COMPUTER SERVICES</span>
  </div>

  <p class="tagline">Reliable Systems • Friendly Experts • Dependable Results</p>

  <h1 class="salutation">Dear Mr. Ostrander,</h1>

  <div class="letter-body">
    <p>A letterhead is the heading at the top of a sheet of letter paper (stationery). That heading usually consists of a name and an address, and a logo or corporate design, and sometimes a background pattern.</p>
    <p>The term "letterhead" is often used to refer to the whole sheet imprinted with such a heading. Many companies and individuals prefer to create a letterhead template in a word processor or other software application. This generally includes the same information as pre-printed stationery but without the additional costs involved.</p>
    <p>Letterhead can then be printed on stationery (or plain paper) as needed on a local output device or sent electronically. That heading usually consists of a name and an address, and a logo or corporate design, and sometimes a background pattern. The term "letterhead" is often used to refer to the whole sheet imprinted with such a heading.</p>
  </div>

  <p class="sign-off closing">Sincerely,</p>
  <p class="sign-off name">Owen Mercer</p>
  <p class="sign-off title">Director</p>

  <p class="contact phone">
    <svg viewBox="0 0 24 24"><path d="M6.6 10.8c1.4 2.8 3.8 5.1 6.6 6.6l2.2-2.2c.3-.3.7-.4 1-.2 1.1.4 2.3.6 3.6.6.6 0 1 .4 1 1V20c0 .6-.4 1-1 1C10.6 21 3 13.4 3 4c0-.6.4-1 1-1h3.5c.6 0 1 .4 1 1 0 1.3.2 2.5.6 3.6.1.3 0 .7-.2 1z"/></svg>
    802-555-0147
  </p>
  <p class="contact address">
    <svg viewBox="0 0 24 24"><path d="M12 3 1.5 12h3v9h6v-6h3v6h6v-9h3zM17 5h2.5v4.5L17 7.3z"/></svg>
    47 Fernwick Hollow Road, Ashbury Falls, VT 05999
  </p>
  <p class="website">www.Larkvale.example</p>
</div>
</body>
</html>
```